Wellness Company needs 2 updated pages for our powerpoint

1 page of our powerpoint needs to be split into 2 pages. I have uploaded an image of it all on 1 page, the left side needs to be on 1 page and the right side needs to be on a separate page. I also uploaded images of the top & bottom since it is so blurry. Landscape view, please. Don't worry about the bottom of the page design since that is our template.

Target Market(s)

Wellness and Business

Industry/Entity Type

Health And Wellness

Requirements
Must have
• Clear wording and bold font.
Nice to have
• Clear circles and images

```html
<!DOCTYPE html>
<html lang="en">
<head>
<meta charset="utf-8">
<title>Compensation Plan at a Glance</title>
<link href="https://fonts.googleapis.com/css2?family=Arimo:wght@400;700&display=swap" rel="stylesheet">
<style>
:root{
  --stage:#d9d9d9;
  --paper:#ffffff;
  --green:#6aa51e;
  --green-light:#8dc63f;
  --green-dark:#4f8a10;
  --orange:#f0a21a;
  --orange-deep:#d9690b;
  --ink:#6b6b6b;
  --rule:#cfcfcf;
}
*{box-sizing:border-box;margin:0;padding:0}
html,body{width:1200px;height:707px;overflow:hidden;background:var(--stage)}
body{font-family:"Arimo",Arial,sans-serif;color:var(--ink)}
.canvas{position:relative;width:1200px;height:707px;background:var(--stage)}
.slide{position:absolute;width:572px;height:332px;background:var(--paper);overflow:hidden}
.slide-a{left:25px;top:25px}
.slide-b{left:614px;top:25px}
.slide-c{left:25px;top:361px}
.slide-d{left:614px;top:361px}
.abs{position:absolute}

/* brand frame */
.brand{position:absolute}
.brand-bar{position:absolute;left:0;right:0;top:26%;height:48%;border:1px solid var(--green);background:var(--paper)}
.brand-mark{position:absolute;left:37%;width:28%;top:0;bottom:0;border:1px solid var(--green);background:var(--paper);display:flex;align-items:center;justify-content:center;text-align:center;color:var(--green);font-weight:700;line-height:1.05;letter-spacing:.5px}
.brand-label{position:absolute;top:26%;height:48%;display:flex;align-items:center;color:var(--orange)}
.brand-left{left:4%}
.brand-right{right:5%}

/* headers */
.bar{position:absolute;background:var(--green-light);color:#fff;font-weight:700;display:flex;align-items:center;justify-content:center}
.bar .num{position:absolute;left:6px;font-size:13px}

/* direct selling */
.panel{position:absolute;background:var(--paper)}
.panel.framed{border:1px solid var(--green-light)}
.panel.shadow{border:1px solid #c8c8c8;box-shadow:2px 2px 5px rgba(0,0,0,.25)}
.tagline{color:var(--orange);text-align:center}
.price-row{display:flex;justify-content:space-between;color:var(--green);border-bottom:1px solid var(--rule)}
.keep-row{display:flex;justify-content:space-between;background:var(--green);color:#fff}
.note{text-align:center;color:var(--orange)}
.fast-art{position:absolute;left:0;top:0}

/* leadership */
.lead-col{position:absolute;font-size:6.3px;line-height:1.2;color:#555;text-align:justify}

/* rank band */
.ranks{position:absolute;left:0;right:0;top:230px;height:102px;background:var(--green);display:flex}
.slide-a .ranks{top:224px;height:108px}
.rank{flex:1;padding:3px 4px;border-right:1px dashed rgba(255,255,255,.8);color:#fff}
.rank:last-child{border-right:0}
.rank h4{font-size:6.6px;line-height:1.15;text-align:center;font-weight:700;border-bottom:1px solid rgba(255,255,255,.8);padding-bottom:3px;margin-bottom:3px}
.rank li{list-style:none;font-size:6.3px;line-height:1.18;padding-left:7px;position:relative;margin-bottom:1px}
.rank li::before{content:"\2713";position:absolute;left:0;top:0}

/* step marker */
.step{position:absolute;width:34px;height:34px;border:2px solid var(--orange);border-radius:50%;color:var(--orange);font-size:15px;display:flex;align-items:center;justify-content:center}

/* unilevel */
.uni-title{position:absolute;left:31px;top:33px;font-size:15px;font-weight:700;color:var(--green-light)}
.uni-head{position:absolute;top:65px;font-size:9.5px;font-weight:700;color:var(--orange);text-align:center}
.uni-row{position:absolute;left:18px;font-size:9px;color:var(--orange)}
.uni-bar{position:absolute;top:78px;background:var(--green);color:#fff;display:flex;justify-content:center;padding-top:6px;font-size:14px}
.uni-top{position:absolute;background:var(--orange);color:#fff;font-size:9px;display:flex;align-items:center;justify-content:center}
.uni-note{position:absolute;left:325px;top:112px;width:247px;height:73px;background:#efefef;padding:12px 10px;font-size:7.3px;line-height:1.3;color:#222}
</style>
</head>
<body>
<div class="canvas">

<!-- ============ SLIDE A : combined overview ============ -->
<section class="slide slide-a">
  <div class="panel framed" style="left:18px;top:18px;width:174px;height:112px">
    <div class="bar" style="left:0;top:0;width:172px;height:15px;font-size:8.5px;background:var(--green-light)"><span class="num">1</span>Direct Selling</div>
    <p class="tagline" style="margin-top:22px;font-size:8px">Sell the product. Keep the profit.</p>
    <div class="price-row" style="margin:7px 10px 0;font-size:8.5px;padding-bottom:2px"><span>Suggested Retail:</span><span>$34.95</span></div>
    <div class="price-row" style="margin:6px 10px 0;font-size:8.5px;padding-bottom:2px"><span>Wholesale:</span><span>$24.95</span></div>
    <div class="keep-row" style="margin:7px 8px 0;font-size:8.5px;padding:2px 5px"><span>You keep</span><span>$10.00</span></div>
  </div>
  <div class="panel framed" style="left:18px;top:134px;width:174px;height:90px">
    <div class="bar" style="left:0;top:0;width:172px;height:15px;font-size:8.5px"><span class="num">2</span>Fast Start Bonus</div>
    <svg class="fast-art" width="172" height="90" viewBox="0 0 172 90" aria-hidden="true">
      <defs><radialGradient id="orbA" cx="40%" cy="35%" r="70%"><stop offset="0" stop-color="#f6b23a"/><stop offset="1" stop-color="#cf5c08"/></radialGradient></defs>
      <g stroke="#f0a21a" stroke-width="1.5"><line x1="87" y1="29" x2="33" y2="45"/><line x1="87" y1="29" x2="87" y2="51"/><line x1="87" y1="29" x2="141" y2="45"/></g>
      <g fill="url(#orbA)"><circle cx="87" cy="27" r="10"/><circle cx="33" cy="45" r="10"/><circle cx="87" cy="52" r="10"/><circle cx="141" cy="45" r="10"/></g>
      <g fill="#fff" font-size="7.5" text-anchor="middle" font-family="Arimo,Arial,sans-serif"><text x="87" y="30">YOU</text><text x="33" y="48">$10</text><text x="87" y="55">$20</text><text x="141" y="48">$40</text></g>
    </svg>
    <p class="note" style="position:absolute;top:66px;left:4px;right:4px;font-size:6.6px;line-height:1.25;color:#555">Earn up to $40 for each silver, gold or platinum package you sell</p>
  </div>

  <div class="brand" style="left:236px;top:9px;width:277px;height:60px">
    <div class="brand-bar"></div>
    <div class="brand-label brand-left" style="font-size:10px">Compensation Plan</div>
    <div class="brand-label brand-right" style="font-size:10px">At a Glance</div>
    <div class="brand-mark" style="font-size:9px">FERNWAY<br>WELLNESS</div>
  </div>

  <div class="bar" style="left:201px;top:75px;width:371px;height:16px;font-size:8.5px"><span class="num">3</span>Leadership Bonus</div>
  <svg class="abs" style="left:201px;top:93px" width="371" height="70" viewBox="0 0 371 70" aria-hidden="true">
    <defs>
      <radialGradient id="orbL" cx="40%" cy="35%" r="70%"><stop offset="0" stop-color="#f6b23a"/><stop offset="1" stop-color="#cf5c08"/></radialGradient>
      <radialGradient id="orbG" cx="40%" cy="35%" r="70%"><stop offset="0" stop-color="#a8d65a"/><stop offset="1" stop-color="#5e9a16"/></radialGradient>
    </defs>
    <g stroke="#d9d9d9"><line x1="123" y1="0" x2="123" y2="70"/><line x1="247" y1="0" x2="247" y2="70"/></g>
    <g stroke="#f0a21a" stroke-width="1.3">
      <line x1="61" y1="18" x2="22" y2="50"/><line x1="61" y1="18" x2="61" y2="50"/><line x1="61" y1="18" x2="100" y2="50"/>
      <line x1="185" y1="18" x2="146" y2="50"/><line x1="185" y1="18" x2="185" y2="50"/><line x1="185" y1="18" x2="224" y2="50"/>
      <line x1="309" y1="18" x2="270" y2="50"/><line x1="309" y1="18" x2="309" y2="50"/><line x1="309" y1="18" x2="348" y2="50"/>
    </g>
    <g fill="url(#orbG)"><circle cx="61" cy="18" r="14"/><circle cx="185" cy="18" r="14"/><circle cx="309" cy="18" r="14"/></g>
    <g fill="url(#orbL)">
      <circle cx="22" cy="52" r="13"/><circle cx="61" cy="50" r="13"/><circle cx="100" cy="52" r="13"/>
      <circle cx="146" cy="52" r="13"/><circle cx="185" cy="50" r="13"/><circle cx="224" cy="52" r="13"/>
      <circle cx="270" cy="52" r="13"/><circle cx="309" cy="50" r="13"/><circle cx="348" cy="52" r="13"/>
    </g>
    <g fill="#fff" font-size="8.5" text-anchor="middle" font-family="Arimo,Arial,sans-serif">
      <text x="61" y="21">MBO</text><text x="185" y="21">SBO</text><text x="309" y="21">EBO</text>
      <text x="22" y="55">$40</text><text x="61" y="53">$20</text><text x="100" y="55">$10</text>
      <text x="146" y="55">$80</text><text x="185" y="53">$40</text><text x="224" y="55">$20</text>
      <text x="270" y="55">$160</text><text x="309" y="53">$80</text><text x="348" y="55">$40</text>
    </g>
  </svg>
  <p class="lead-col" style="left:208px;top:176px;width:112px">MBOs earn up to $10, $20 or $40 per enrollment package sold</p>
  <p class="lead-col" style="left:330px;top:176px;width:114px">SBOs earn up to $20, $40 or $80 for every enrollment package sold. SBO leadership bonus may be split between different leaders. MBOs and SBOs will split the difference between bonuses.</p>
  <p class="lead-col" style="left:454px;top:176px;width:112px">EBOs earn up to $40, $80 or $160 for every enrollment package sold. EBO leadership bonus can be split between leaders. MBOs, SBOs and EBOs will split the difference between bonuses.</p>

  <div class="ranks">
    <div class="rank"><h4>1. Independent Business Owner (IBO)</h4><ul><li>Enroll as an Active Independent Business Owner</li><li>After your first month to remain active you must personally maintain a minimum of 25 business volume &amp; subscribe to autoship</li></ul></div>
    <div class="rank"><h4>2. Managing Business Owner (MBO)</h4><ul><li>Be an active IBO and personally maintain 50 business volume</li><li>Personally Sponsor 3 IBO's. Each of them must be active</li></ul></div>
    <div class="rank"><h4>3. Senior Business Owner (SBO)</h4><ul><li>Be an Active IBO and personally acquire 100 business volume</li><li>Promote 3 MBO's in 3 Separate Legs</li><li>Maintain 1500 combined business volume for entire downline</li></ul></div>
    <div class="rank"><h4>4. Executive Business Owner (EBO)</h4><ul><li>Be an Active IBO and personally maintain 200 business volume</li><li>Promote 3 SBO's in 3 Separate Legs</li><li>Maintain 5000 combined business volume for entire downline</li></ul></div>
    <div class="rank"><h4>5. Regional Executive Business Owner (REBO)</h4><ul><li>Be an Active IBO and personally maintain 400 business volume</li><li>Promote 3 SBO's in 3 Separate Legs</li><li>Maintain 15000 combined business volume for entire downline</li></ul></div>
  </div>
</section>

<!-- ============ SLIDE B : refined overview ============ -->
<section class="slide slide-b">
  <div class="bar" style="left:18px;top:18px;width:174px;height:20px;font-size:10px"><span class="num" style="font-size:14px;left:8px">1</span>Direct Selling</div>
  <div class="panel shadow" style="left:18px;top:42px;width:174px;height:100px">
    <p class="tagline" style="margin-top:8px;font-size:9px">Sell the product. Keep the profit.</p>
    <div class="price-row" style="margin:8px 10px 0;font-size:9px;padding-bottom:2px"><span>Suggested Retail:</span><span>$34.95</span></div>
    <div class="price-row" style="margin:6px 10px 0;font-size:9px;padding-bottom:2px"><span>Wholesale:</span><span>$24.95</span></div>
    <div class="keep-row" style="margin:7px 10px 0;font-size:9px;padding:2px 5px"><span>You keep</span><span>$10.00</span></div>
  </div>
  <div class="abs" style="left:18px;top:146px;width:174px;height:3px;background:var(--green-light)"></div>
  <div class="bar" style="left:18px;top:156px;width:174px;height:20px;font-size:10px"><span class="num" style="font-size:14px;left:8px">2</span>Fast Start Bonus</div>
  <div class="panel shadow" style="left:18px;top:182px;width:174px;height:128px">
    <svg class="fast-art" width="172" height="128" viewBox="0 0 172 128" aria-hidden="true">
      <g stroke="#f0a21a" stroke-width="1.5"><line x1="87" y1="30" x2="30" y2="58"/><line x1="87" y1="30" x2="87" y2="58"/><line x1="87" y1="30" x2="144" y2="58"/></g>
      <circle cx="87" cy="22" r="16" fill="#f0a21a"/>
      <g fill="#fff" stroke="#f0a21a" stroke-width="2.5"><circle cx="26" cy="65" r="15"/><circle cx="87" cy="74" r="15"/><circle cx="146" cy="65" r="15"/></g>
      <g font-size="10" text-anchor="middle" font-family="Arimo,Arial,sans-serif"><text x="87" y="26" fill="#fff">YOU</text><text x="26" y="69" fill="#f0a21a">$10</text><text x="87" y="78" fill="#f0a21a">$20</text><text x="146" y="69" fill="#f0a21a">$40</text></g>
    </svg>
    <p class="note" style="position:absolute;top:98px;left:4px;right:4px;font-size:8.4px;line-height:1.3">Earn up to $40 for each silver, gold or platinum package you sell</p>
  </div>
  <div class="abs" style="left:18px;top:314px;width:174px;height:3px;background:var(--green-light)"></div>

  <div class="brand" style="left:210px;top:6px;width:344px;height:74px">
    <div class="brand-bar"></div>
    <div class="brand-label brand-left" style="font-size:11px">Compensation Plan</div>
    <div class="brand-label brand-right" style="font-size:11px">At a Glance</div>
    <div class="brand-mark" style="font-size:11px">FERNWAY<br>WELLNESS</div>
  </div>

  <div class="bar" style="left:212px;top:87px;width:351px;height:20px;font-size:10px"><span class="num" style="font-size:14px;left:10px">3</span>Leadership Bonus</div>
  <div class="panel shadow" style="left:212px;top:107px;width:351px;height:208px">
    <svg class="fast-art" width="349" height="135" viewBox="0 0 349 135" aria-hidden="true">
      <g stroke="#d9d9d9"><line x1="116" y1="6" x2="116" y2="200"/><line x1="233" y1="6" x2="233" y2="200"/></g>
      <g stroke="#f0a21a" stroke-width="1.5">
        <line x1="26" y1="64" x2="67" y2="29"/><line x1="26" y1="64" x2="67" y2="64"/><line x1="26" y1="64" x2="67" y2="103"/>
        <line x1="143" y1="64" x2="184" y2="29"/><line x1="143" y1="64" x2="184" y2="64"/><line x1="143" y1="64" x2="184" y2="103"/>
        <line x1="260" y1="64" x2="301" y2="29"/><line x1="260" y1="64" x2="301" y2="64"/><line x1="260" y1="64" x2="301" y2="103"/>
      </g>
      <g fill="#f0a21a"><circle cx="26" cy="64" r="17"/><circle cx="143" cy="64" r="17"/><circle cx="260" cy="64" r="17"/></g>
      <g fill="#fff" stroke="#f0a21a" stroke-width="2.5">
        <circle cx="67" cy="29" r="14"/><circle cx="67" cy="64" r="14"/><circle cx="67" cy="103" r="14"/>
        <circle cx="184" cy="29" r="14"/><circle cx="184" cy="64" r="14"/><circle cx="184" cy="103" r="14"/>
        <circle cx="301" cy="29" r="14"/><circle cx="301" cy="64" r="14"/><circle cx="301" cy="103" r="14"/>
      </g>
      <g font-size="9.5" text-anchor="middle" font-family="Arimo,Arial,sans-serif" fill="#f0a21a">
        <text x="67" y="33">$10</text><text x="67" y="68">$20</text><text x="67" y="107">$40</text>
        <text x="184" y="33">$20</text><text x="184" y="68">$40</text><text x="184" y="107">$80</text>
        <text x="301" y="33">$40</text><text x="301" y="68">$80</text><text x="301" y="107">$160</text>
      </g>
      <g font-size="8.5" text-anchor="middle" font-family="Arimo,Arial,sans-serif" fill="#fff"><text x="26" y="67">MBO</text><text x="143" y="67">SBO</text><text x="260" y="67">EBO</text></g>
    </svg>
    <p class="lead-col" style="left:6px;top:136px;width:106px;font-size:7.3px">MBOs earn up to $10, $20 or $40 per enrollment package sold</p>
    <p class="lead-col" style="left:122px;top:136px;width:106px;font-size:7px">SBOs earn up to $20, $40 or $80 for every enrollment package sold. SBO leadership bonus may be split between different leaders. MBOs and SBOs will split the difference between bonuses.</p>
    <p class="lead-col" style="left:239px;top:136px;width:106px;font-size:7px">EBOs earn up to $40, $80 or $160 for every enrollment package sold. EBO leadership bonus can be split between leaders. MBOs, SBOs and EBOs will split the difference between bonuses.</p>
  </div>
</section>

<!-- ============ SLIDE C : direct selling & fast start ============ -->
<section class="slide slide-c">
  <div class="brand" style="left:156px;top:12px;width:267px;height:59px">
    <div class="brand-bar"></div>
    <div class="brand-label brand-left" style="font-size:9.5px;color:var(--orange);font-weight:700">Compensation Plan</div>
    <div class="brand-label brand-right" style="font-size:9.5px;color:var(--orange);font-weight:700">At a Glance</div>
    <div class="brand-mark" style="font-size:8.5px">FERNWAY<br>WELLNESS</div>
  </div>
  <div class="bar" style="left:0;top:85px;width:572px;height:18px;font-size:9px;justify-content:flex-start">
    <span style="position:absolute;left:158px">Direct Selling</span>
    <span style="position:absolute;left:396px">Fast Start Bonus</span>
  </div>

  <div class="step" style="left:38px;top:138px">1</div>
  <div class="panel shadow" style="left:87px;top:113px;width:174px;height:103px">
    <p class="tagline" style="margin-top:6px;font-size:8.5px">Sell the product. Keep the profit.</p>
    <div class="price-row" style="margin:9px 10px 0;font-size:10px;padding-bottom:2px"><span>Suggested Retail:</span><span>$34.95</span></div>
    <div class="price-row" style="margin:6px 10px 0;font-size:10px;padding-bottom:2px"><span>Wholesale:</span><span>$24.95</span></div>
    <div class="keep-row" style="margin:8px 10px 0;font-size:9px;padding:2px 5px"><span>You keep</span><span>$10.00</span></div>
  </div>
  <div class="abs" style="left:90px;top:221px;width:168px;height:3px;background:var(--green-light)"></div>

  <div class="step" style="left:291px;top:138px">2</div>
  <div class="panel shadow" style="left:346px;top:113px;width:161px;height:103px">
    <svg class="fast-art" width="159" height="103" viewBox="0 0 159 103" aria-hidden="true">
      <defs><radialGradient id="orbC" cx="40%" cy="35%" r="70%"><stop offset="0" stop-color="#f6b23a"/><stop offset="1" stop-color="#cf5c08"/></radialGradient></defs>
      <g stroke="#f0a21a" stroke-width="1.5"><line x1="91" y1="22" x2="45" y2="45"/><line x1="91" y1="22" x2="91" y2="50"/><line x1="91" y1="22" x2="140" y2="45"/></g>
      <g fill="url(#orbC)"><circle cx="91" cy="18" r="12"/><circle cx="45" cy="45" r="11"/><circle cx="91" cy="54" r="11"/><circle cx="140" cy="45" r="11"/></g>
      <g fill="#fff" font-size="8" text-anchor="middle" font-family="Arimo,Arial,sans-serif"><text x="91" y="21">YOU</text><text x="45" y="48">$10</text><text x="91" y="57">$20</text><text x="140" y="48">$40</text></g>
    </svg>
    <p class="note" style="position:absolute;top:76px;left:4px;right:4px;font-size:7.5px;line-height:1.3;color:var(--green-dark)">Earn up to $40 for each silver, gold or platinum package you sell</p>
  </div>
  <div class="abs" style="left:349px;top:221px;width:155px;height:3px;background:var(--green-light)"></div>

  <div class="ranks">
    <div class="rank"><h4>1. Independent Business Owner (IBO)</h4><ul><li>Enroll as an Active Independent Business Owner</li><li>After your first month to remain active you must personally maintain a minimum of 25 business volume &amp; subscribe to autoship</li></ul></div>
    <div class="rank"><h4>2. Managing Business Owner (MBO)</h4><ul><li>Be an active IBO and personally maintain 50 business volume</li><li>Personally Sponsor 3 IBO's. Each of them must be active</li></ul></div>
    <div class="rank"><h4>3. Senior Business Owner (SBO)</h4><ul><li>Be an Active IBO and personally acquire 100 business volume</li><li>Promote 3 MBO's in 3 Separate Legs</li><li>Maintain 1500 combined business volume for entire downline</li></ul></div>
    <div class="rank"><h4>4. Executive Business Owner (EBO)</h4><ul><li>Be an Active IBO and personally maintain 200 business volume</li><li>Promote 3 SBO's in 3 Separate Legs</li><li>Maintain 5000 combined business volume for entire downline</li></ul></div>
    <div class="rank"><h4>5. Regional Executive Business Owner (REBO)</h4><ul><li>Be an Active IBO and personally maintain 400 business volume</li><li>Promote 3 SBO's in 3 Separate Legs</li><li>Maintain 15000 combined business volume for entire downline</li></ul></div>
  </div>
</section>

<!-- ============ SLIDE D : unilevel commission ============ -->
<section class="slide slide-d">
  <h2 class="uni-title">Unilevel Commission</h2>
  <div class="brand" style="left:338px;top:32px;width:207px;height:45px">
    <div class="brand-bar"></div>
    <div class="brand-label brand-left" style="font-size:7px">Compensation Plan</div>
    <div class="brand-label brand-right" style="font-size:7px">At a Glance</div>
    <div class="brand-mark" style="font-size:6.5px">FERNWAY<br>WELLNESS</div>
  </div>

  <div class="uni-head" style="left:30px;width:65px">IBO</div>
  <div class="uni-head" style="left:95px;width:79px">MBO</div>
  <div class="uni-head" style="left:174px;width:77px">SBO</div>
  <div class="uni-head" style="left:252px;width:71px">EBO\REBO</div>

  <div class="uni-row" style="top:80px">1</div>
  <div class="uni-row" style="top:97px">2</div>
  <div class="uni-row" style="top:115px">3</div>
  <div class="uni-row" style="top:132px">4</div>
  <div class="uni-row" style="top:150px">5</div>
  <div class="uni-row" style="top:167px">6</div>
  <div class="uni-row" style="top:185px">7</div>
  <div class="uni-row" style="top:202px">8</div>

  <div class="uni-bar" style="left:30px;width:64px;height:35px">5%</div>
  <div class="uni-bar" style="left:95px;width:78px;height:70px;padding-top:9px;font-size:15px">5%</div>
  <div class="uni-bar" style="left:174px;width:77px;height:104px;padding-top:18px;font-size:15px">5%</div>
  <div class="uni-bar" style="left:252px;width:71px;height:122px;padding-top:26px;font-size:15px">5%</div>
  <div class="uni-top" style="left:252px;top:200px;width:71px;height:18px">10%</div>

  <div class="uni-note">IBOs earn 5% commission on all sales 2 levels deep.<br>MBOs earn 5% commission on all sales 4 levels deep.<br>SBOs earn 5% commission on all sales 6 levels deep.<br>EBOs earn 5% commission on all sales 7 levels deep and 10% on the 8<sup>th</sup> level.</div>

  <div class="ranks">
    <div class="rank"><h4>1. Independent Business Owner (IBO)</h4><ul><li>Enroll as an Active Independent Business Owner</li><li>After your first month to remain active you must personally maintain a minimum of 25 business volume &amp; subscribe to autoship</li></ul></div>
    <div class="rank"><h4>2. Managing Business Owner (MBO)</h4><ul><li>Be an active IBO and personally maintain 50 business volume</li><li>Personally Sponsor 3 IBO's. Each of them must be active</li></ul></div>
    <div class="rank"><h4>3. Senior Business Owner (SBO)</h4><ul><li>Be an Active IBO and personally acquire 100 business volume</li><li>Promote 3 MBO's in 3 Separate Legs</li><li>Maintain 1500 combined business volume for entire downline</li></ul></div>
    <div class="rank"><h4>4. Executive Business Owner (EBO)</h4><ul><li>Be an Active IBO and personally maintain 200 business volume</li><li>Promote 3 SBO's in 3 Separate Legs</li><li>Maintain 5000 combined business volume for entire downline</li></ul></div>
    <div class="rank"><h4>5. Regional Executive Business Owner (REBO)</h4><ul><li>Be an Active IBO and personally maintain 400 business volume</li><li>Promote 3 SBO's in 3 Separate Legs</li><li>Maintain 15000 combined business volume for entire downline</li></ul></div>
  </div>
</section>

</div>
</body>
</html>
```